Дизайн этикетки и упаковки лечебной косметики
Задание на дизайн
Приоритеты объектов в упаковке
Зонтичная марка, Вид продукта, Название продукта
Опишите свою организацию или продукт и целевую аудиторию
Продукция представляет собой линейку новой лечебной косметики (космецевтики) под брендом (зонтичная марка) «Vok Lab», направленную на решение проблем при повреждениях кожи (раны, ссадины, незначительные ожоги, угревая сыпь в стадии воспаления и после вскрытия прыщей) и слизистой оболочки рта (воспаления, раны, укрепление десен и др., после стоматологических операций и имплантаций), а также после бритья и косметических манипуляций (чистка лица, пилинг, депиляция, татуаж, мезотерапия, бритье, маникюр, педикюр и др.). Эффект продуктов обусловлен инновационным комплексом «Zentrava» и дополнен веществами, способствующими восстановлению и регенерации кожи и слизистой.
Название продуктов:
- Бальзам для полости рта Заживление + Регенерация
- Сыворотка для проблемной и поврежденной кожи Заживление + Регенерация
Целевая аудитория сыворотки для кожи – преимущественно женский пол от 16 до 40, имеющие проблемы с кожей, а также женщины от 35 и старше, для которых важна забота о себе и регулярно делающие косметические манипуляции с нарушением кожных покровов (пилинг, депиляция и т.д.).
Целевая аудитория бальзама – преимущественно люди обоих полов, от 30 и старше.
Ценовой сегмент – средний.
Продукция на рынке новая. Продажи в первое время – через маркетплейсы. Выпускается во флаконах коричневого цвета с черной крышкой по 50 мл.
ЗАДАЧА: разработать запоминающийся, привлекающий внимание, «продающий» дизайн упаковки и этикетки для продукции, ассоциирующейся со здоровьем, надежностью, качеством, инновационностью, современностью.
Вся информация тут: https://files.quorvani-docs.net/d/8Kx4TqWbLp2RzN7vYeHs3JdUcGa/view?share=open&uid=552901873460218837412&fmt=full
К предложенным образцам не обязательно привязываться, интересней предложить собственную концепцию
Комментарии и пожелания для дизайнеров
Дизайн коробок и этикеток должен быть выполнен в одном стиле, но каждый продукт должен быть узнаваем за счет цвета и/или дополнительных элементов, например, рисунка, графики. Цветовая гамма – на усмотрение дизайнера. Желательно не менее трех цветов.
Коробка – четыре одинаковые плоскости, верх (крышка), дно. Основные плоскости: высота – 119 мм, ширина – 38 мм. Крышка и дно: 38×38 мм
Этикетка круговая, может быть разделена на несколько частей. Пропорции деления определяются дизайном.
Этикетка сыворотка: высота – 41 мм, длина – 114 мм
Этикетка бальзам: высота – 59 мм, длина – 101 мм
Выпускается во флаконах коричневого цвета с черной крышкой по 50 мл.
Название бренда выполняется в виде подписи «With care — Vok Lab». Подпись должна быть выполнена как бы «от руки», расположена внизу этикетки и коробки, не должна превалировать над остальными элементами, но быть хорошо видимой. Возможно, под небольшим уклоном.
Главными элементами должны быть: вид продукции (бальзам, сыворотка), слоган Заживление + Регенерация и указание активного комплекса Zentrava.
Шрифты подбирает/разрабатывает дизайнер самостоятельно.
Дополнительные требования тут: https://files.quorvani-docs.net/d/8Kx4TqWbLp2RzN7vYeHs3JdUcGa/view?share=open&uid=552901873460218837412&fmt=full

```html
<!DOCTYPE html>
<html lang="ru">
<head>
<meta charset="utf-8">
<title>Сыворотка — упаковка и этикетка</title>
<link href="https://fonts.googleapis.com/css2?family=Comfortaa:wght@400;500;600&display=swap" rel="stylesheet">
<style>
  :root {
    --bg: #f4f4f6;
    --box: #414554;
    --box-side: #3b3f4d;
    --lilac: #c9c6f2;
    --label: #c8c8ec;
    --ink: #17171c;
    --rule-dark: #8d8ab8;
    --rule-light: #a9a6c9;
  }
  * { box-sizing: border-box; margin: 0; padding: 0; }
  html, body { width: 1200px; height: 1055px; overflow: hidden; }
  body {
    background: var(--bg);
    font-family: "Comfortaa", sans-serif;
    position: relative;
  }

  /* Box: front face + side face, unfolded flat */
  .box { position: absolute; left: 170px; top: 150px; display: flex; }
  .box-face {
    width: 250px; height: 780px;
    background: var(--box);
    color: var(--lilac);
    position: relative;
    overflow: hidden;
  }
  .box-face--side { background: var(--box-side); }

  .front-copy {
    position: absolute; top: 270px; left: 0; right: 0;
    text-align: center;
  }
  .product-type { font-size: 25px; font-weight: 600; letter-spacing: .3px; }
  .product-for { font-size: 14.5px; line-height: 1.25; margin-top: 6px; }
  .slogan { font-size: 14.5px; margin-top: 22px; }
  .sparkle { display: block; margin: 14px auto 12px; }
  .complex { font-size: 14.5px; line-height: 1.22; }
  .rule { width: 80px; height: 1px; margin: 18px auto 16px; }
  .box-face .rule { background: var(--rule-dark); }
  .volume { font-size: 16px; }
  .signature {
    font-size: 17px; font-weight: 400;
    margin-top: 30px;
  }

  .batch {
    position: absolute; left: 28px; bottom: 85px;
    font-size: 10.5px; line-height: 2.35;
  }

  .side-copy {
    position: absolute; top: 150px; right: 60px;
    height: 480px;
    writing-mode: vertical-rl;
    font-size: 10px; line-height: 1.9;
  }
  .side-copy p + p { margin-right: 18px; }

  /* Bottle label, unrolled */
  .label {
    position: absolute; left: 740px; top: 270px;
    width: 330px; height: 540px;
    background: var(--label);
    color: var(--ink);
    text-align: center;
    padding-top: 72px;
  }
  .label .product-type { font-size: 26px; }
  .label .rule { background: var(--rule-light); }
</style>
</head>
<body>

<div class="box">
  <section class="box-face box-face--front">
    <div class="front-copy">
      <h1 class="product-type">Сыворотка</h1>
      <p class="product-for">для проблемной<br>и поврежденной кожи</p>
      <p class="slogan">Заживление + Регенерация</p>
      <svg class="sparkle" width="34" height="40" viewBox="0 0 34 40" aria-hidden="true">
        <path d="M17 0 Q19 18 34 20 Q19 22 17 40 Q15 22 0 20 Q15 18 17 0Z" fill="var(--lilac)"/>
      </svg>
      <p class="complex">На основе инновационного<br>активного комплекса<br>«Zentrava»</p>
      <div class="rule"></div>
      <p class="volume">50 мл</p>
      <p class="signature">With care — Vok Lab</p>
    </div>
    <div class="batch">
      <p>Номер партии</p>
      <p>Дата изготовления</p>
      <p>Годен до:</p>
    </div>
  </section>
  <section class="box-face box-face--side">
    <div class="side-copy">
      <p>Состав: вода, глицерин, пантенол, аллантоин, комплекс Zentrava.</p>
      <p>Нанесите на чистую кожу.</p>
      <p>Хранить при температуре до 25 °C</p>
    </div>
  </section>
</div>

<section class="label">
  <h2 class="product-type">Сыворотка</h2>
  <p class="product-for">для проблемной<br>и поврежденной кожи</p>
  <p class="slogan">Заживление + Регенерация</p>
  <svg class="sparkle" width="34" height="40" viewBox="0 0 34 40" aria-hidden="true">
    <path d="M17 0 Q19 18 34 20 Q19 22 17 40 Q15 22 0 20 Q15 18 17 0Z" fill="var(--ink)"/>
  </svg>
  <p class="complex">На основе инновационного<br>активного комплекса<br>«Zentrava»</p>
  <div class="rule"></div>
  <p class="volume">50 мл</p>
  <p class="signature">With care — Vok Lab</p>
</section>

</body>
</html>
```